Lullio.com re-design on Wix platform

Re-do this website : www.lullio.com
Lullio is a sound conditioner that uses the calming, sedative qualities of mundane rhythmic stimulation to allow its users to rest easier and deeper than they normally would.
I think of Lullio.com as a web app; a place to use and buy the product. Im open to suggestion on site layouts, whether you use one page or several.
Use the same color scheme: purple, white, black, grey/silver
I would like a place for testimonials, even though you don't currently see one on the site. Other than that, assume the content will stay mostly the same.
I'd like a clean, modern, professional look. The site will reside on Wix platform.

```html
<!DOCTYPE html>
<html lang="en">
<head>
<meta charset="utf-8">
<title>Lullio — Sleep Tips</title>
<link href="https://fonts.googleapis.com/css2?family=EB+Garamond:wght@400&family=Nunito+Sans:wght@400;600&display=swap" rel="stylesheet">
<style>
  :root {
    --header-grey: #4f4f4f;
    --page-grey: #e6e6e6;
    --purple: #a400a8;
    --ink: #111111;
    --white: #ffffff;
    --muted: #9a9a9a;
  }
  * { margin: 0; padding: 0; box-sizing: border-box; }
  html, body {
    width: 1163px; height: 1200px; overflow: hidden;
    background: var(--page-grey);
    font-family: "Nunito Sans", Arial, sans-serif;
    color: var(--ink);
  }
  .page { position: relative; width: 1163px; height: 1200px; }

  .site-header {
    position: absolute; left: 0; top: 0; width: 100%; height: 98px;
    background: var(--header-grey);
  }
  .brand {
    position: absolute; left: 84px; top: 22px;
    font-size: 44px; font-weight: 600; color: var(--white);
    letter-spacing: 0.5px; line-height: 1;
  }
  .main-nav a {
    position: absolute; top: 45px;
    font-size: 14px; letter-spacing: 1.6px; color: var(--white);
    text-decoration: none; line-height: 1;
  }
  .main-nav .is-current { color: var(--muted); }

  .section-label {
    position: absolute; left: 0; width: 100%; top: 204px;
    text-align: center; color: var(--purple);
    font-size: 17px; letter-spacing: 2px; line-height: 1;
  }
  .section-rule {
    position: absolute; left: 561px; top: 236px;
    width: 42px; height: 2px; background: var(--purple);
  }
  .headline {
    position: absolute; left: 0; width: 100%; top: 308px;
    text-align: center;
    font-family: "EB Garamond", Georgia, serif; font-weight: 400;
    font-size: 53px; line-height: 1.2; color: var(--ink);
  }

  .tips { position: absolute; top: 467px; list-style: none; }
  .tips-left { left: 141px; width: 410px; }
  .tips-right { left: 624px; width: 450px; }
  .tips li {
    position: relative; padding-left: 11px;
    font-size: 18px; line-height: 30.5px;
    margin-bottom: 30.5px;
  }
  .tips li::before { content: "•"; position: absolute; left: 0; top: 0; }

  .cta {
    position: absolute; left: 425px; top: 1011px;
    width: 314px; height: 68px;
    background: var(--purple); color: var(--white);
    display: flex; align-items: center; justify-content: center;
    font-size: 18px; letter-spacing: 2px; text-decoration: none;
  }
</style>
</head>
<body>
<div class="page">
  <header class="site-header">
    <div class="brand">Lullio</div>
    <nav class="main-nav">
      <a class="is-current" href="#" style="left:370px">HOME</a>
      <a href="#" style="left:467px">ABOUT</a>
      <a href="#" style="left:571px">FREE DEMO</a>
      <a href="#" style="left:702px">TESTIMONIALS</a>
      <a href="#" style="left:872px">SLEEP TIPS</a>
      <a href="#" style="left:1012px">CONTACT</a>
    </nav>
  </header>

  <main>
    <p class="section-label">SLEEP TIPS</p>
    <div class="section-rule"></div>
    <h1 class="headline">Try these tips while listening to Lullio.</h1>

    <ul class="tips tips-left">
      <li>Count the oscillations. Every ten oscillations take a very deep breath, hold it in for an entire cycle, and exhale very slowly.</li>
      <li>Envisage something moving in sync with the oscillations. Examples could be a sheep jump&shy;ing over a fence or a car driving by your house. Make sure to count them.</li>
      <li>Play Lullio through good quality speakers if possible.</li>
      <li>Sleep with your room temperature around 63 degrees farenheit.</li>
    </ul>

    <ul class="tips tips-right">
      <li>Sleep in complete darkness.</li>
      <li>Go to bed at roughly the same time every night.</li>
      <li>Avoid afternoon or evening caffeine.</li>
      <li>Avoid more than one or two alcoholic beverages.</li>
      <li>Try stretching or yoga before bed; a relaxed body is a relaxed mind.</li>
      <li>One or two more tips would even out this list.</li>
    </ul>

    <a class="cta" href="#">TRY THE FREE DEMO</a>
  </main>
</div>
</body>
</html>
```